Simple and Approachable Cover for Pet Expo Company Page

Size: 2000 x 430; looking simply for words "Tenbury HR Consulting" and email address "TenburyHRConsulting@mailvane.com." This is for a cover photo for a company profile page for the Northway Animal Fair, where I am a featured speaker on Employee Communications later this month. You can incorporate the attached photo to the left of the banner ad if you wish. The mood I wish to present is approachable, positive and simple.

Target Market(s)

small pet retail business owners

Industry/Entity Type

Pet Shop

Font styles to use
Serif
Sans Serif

Requirements
Must have
• Email address clearly defined/separated. Easy to read.
Nice to have
• I like the picture that I included; subtle pet paw background is also nice
Should not have
• No paid stock images

```html
<!DOCTYPE html>
<html lang="en">
<head>
<meta charset="utf-8">
<title>Tenbury HR Consulting</title>
<link rel="stylesheet" href="https://fonts.googleapis.com/css2?family=Carlito:wght@400;700&display=swap">
<style>
  :root {
    --bg-light: #e6e6e6;
    --bg-mid: #dcdcdc;
    --brand-red: #a5112c;
    --email-fill: #e29d4f;
    --email-edge: #c98a3f;
    --email-text: #1f1f1f;
    --corner-blue: #2f5d8f;
    --corner-pale: #b9c7d6;
    --photo-warm: #c9a27e;
    --photo-red: #c8303a;
    --photo-blue: #6f84a8;
  }
  html, body {
    margin: 0;
    padding: 0;
    overflow: hidden;
  }
  .banner {
    position: relative;
    width: 1200px;
    height: 258px;
    overflow: hidden;
    background: linear-gradient(180deg, var(--bg-light), var(--bg-mid));
    font-family: "Carlito", "Calibri", Arial, sans-serif;
  }
  .team-photo {
    position: absolute;
    left: 0;
    top: 0;
    width: 430px;
    height: 258px;
    background: linear-gradient(90deg, var(--photo-warm) 0%, var(--photo-red) 35%, var(--photo-blue) 65%, var(--photo-warm) 100%);
    opacity: 0.85;
  }
  .company-name {
    position: absolute;
    left: 446px;
    top: 36px;
    margin: 0;
    font-size: 72px;
    font-weight: 700;
    line-height: 1;
    color: var(--brand-red);
    white-space: nowrap;
    letter-spacing: 0.5px;
  }
  .email-badge {
    position: absolute;
    left: 600px;
    top: 178px;
    width: 430px;
    height: 42px;
    box-sizing: border-box;
    border: 1px solid var(--email-edge);
    border-radius: 5px;
    background: var(--email-fill);
    box-shadow: 1px 2px 2px rgba(0,0,0,0.18);
    display: flex;
    align-items: center;
    justify-content: center;
    font-size: 22px;
    color: var(--email-text);
  }
  .corner-accent {
    position: absolute;
    right: 0;
    bottom: 0;
  }
</style>
</head>
<body>
  <div class="banner">
    <div class="team-photo" role="img" aria-label="Photo of the two consultants seated with their two beagle-type dogs"></div>
    <h1 class="company-name">Tenbury HR Consulting</h1>
    <div class="email-badge">TenburyHRConsulting@mailvane.com</div>
    <svg class="corner-accent" width="76" height="76" viewBox="0 0 76 76" aria-hidden="true">
      <polygon points="76,0 76,76 0,76" fill="var(--corner-pale)"/>
      <polygon points="76,6 76,76 6,76" fill="var(--corner-blue)"/>
    </svg>
  </div>
</body>
</html>
```